Business Card Ayurvedic Massage

I'm starting with my ayurvedic massage business and need a business card design. The design should be inline with my brand/logo as well as with the design of my website (www.lumo-thara.ch).
Front: logo and text "Ayurvedische Massagen"
back: name and adress (see details https://www.lumo-thara.ch/kontakt.html)

```html
<!DOCTYPE html>
<html lang="de">
<head>
<meta charset="utf-8">
<title>lumo-thara – Visitenkarte</title>
<link rel="stylesheet" href="https://fonts.googleapis.com/css2?family=Lora:ital,wght@0,400;0,700;1,700&display=swap">
<style>
  :root {
    --page: #e9e4dc;
    --maroon-dark: #6b0d10;
    --maroon: #8e1519;
    --maroon-light: #a51d22;
    --gold: #e2b13c;
    --gold-light: #f7cf52;
    --gold-dark: #b7821f;
    --cream: #f7eee2;
    --card-w: 780px;
  }
  * { box-sizing: border-box; margin: 0; padding: 0; }
  html, body { width: 1189px; height: 1200px; overflow: hidden; }
  body {
    background: var(--page);
    font-family: "Lora", serif;
    position: relative;
  }
  .card {
    position: absolute;
    left: 204px;
    width: var(--card-w);
    height: 503px;
    border-radius: 26px;
    overflow: hidden;
    box-shadow: 0 6px 18px rgba(0,0,0,.25);
  }
  .card--front { top: 73px; background: var(--maroon-dark); }
  .card--back {
    top: 623px;
    background: radial-gradient(ellipse at 50% 40%, var(--maroon-light), var(--maroon) 70%);
  }
  .gold-rule {
    position: absolute; left: 0; right: 0; height: 8px;
    background: linear-gradient(180deg, var(--gold-light), var(--gold-dark));
  }
  .gold-rule--top { top: 114px; }
  .gold-rule--bottom { top: 380px; }
  .feature-band {
    position: absolute; left: 0; right: 0; top: 122px; height: 258px;
    background: radial-gradient(ellipse at 50% 50%, #a81c22, #8a1418 80%);
  }
  .elephant {
    position: absolute; top: 48px; width: 127px; height: 163px;
    border-radius: 10px;
    background: linear-gradient(160deg, #e8b640, #b9802a 60%, #8e2a1c);
  }
  .elephant--left { left: 149px; }
  .elephant--right { left: 503px; }
  .brand-name {
    position: absolute; left: 0; right: 0; top: 128px;
    text-align: center;
    font-size: 34px; font-weight: 400; letter-spacing: 1px;
    color: var(--gold);
  }
  .contact {
    position: absolute; left: 0; right: 0; top: 138px;
    text-align: center; color: var(--cream);
  }
  .contact__name {
    font-size: 36px; font-weight: 700; color: var(--gold); line-height: 44px;
  }
  .contact__role {
    font-size: 19px; color: var(--gold); line-height: 26px; margin-bottom: 20px;
  }
  .contact__address { font-size: 21px; line-height: 27px; }
  .contact__lines {
    margin-top: 10px; font-size: 21px; line-height: 28px;
    display: flex; justify-content: center; align-items: center; gap: 8px;
  }
  .contact__lines svg { display: block; }
  .contact__web {
    margin-top: 10px; font-size: 19px; font-style: italic; font-weight: 700;
    letter-spacing: 2px; color: var(--gold-dark);
  }
  .gold-band {
    position: absolute; left: 0; right: 0; bottom: 0; height: 24px;
    background: linear-gradient(90deg, var(--gold-dark), var(--gold-light) 25%, var(--gold-dark) 60%, var(--gold-light) 85%, var(--gold-dark));
  }
</style>
</head>
<body>
  <section class="card card--front">
    <div class="gold-rule gold-rule--top"></div>
    <div class="feature-band" role="img" aria-label="Dezentes rotes Damastmuster">
      <div class="elephant elephant--left" role="img" aria-label="Illustration eines geschmückten Elefanten mit Sonnenschirm"></div>
      <p class="brand-name">lumo-thara</p>
      <div class="elephant elephant--right" role="img" aria-label="Illustration eines geschmückten Elefanten mit Sonnenschirm, gespiegelt"></div>
    </div>
    <div class="gold-rule gold-rule--bottom"></div>
  </section>

  <section class="card card--back">
    <div class="contact">
      <h1 class="contact__name">Mira Dalmont</h1>
      <p class="contact__role">Dipl. Ayurveda Massage Praktikerin</p>
      <p class="contact__address">Lindenweg 14<br>CH - 8855 Wangen (SZ)</p>
      <p class="contact__lines">
        <svg width="14" height="20" viewBox="0 0 14 20" aria-hidden="true"><rect x="2" y="2" width="10" height="16" rx="2" fill="none" stroke="var(--gold)" stroke-width="2"/></svg>
        <span>+41 77 000 12 34 |</span>
        <svg width="18" height="14" viewBox="0 0 18 14" aria-hidden="true" style="margin-left:10px"><rect x="1" y="1" width="16" height="12" fill="var(--gold)"/><path d="M1 1 L9 8 L17 1" fill="none" stroke="var(--maroon)" stroke-width="1.5"/></svg>
        <span>info@lumo-thara.ch</span>
      </p>
      <p class="contact__web">www.lumo-thara.ch</p>
    </div>
    <div class="gold-band"></div>
  </section>
</body>
</html>
```